Golden Meadow Kit Social Media Graphics

Focusing on the Golden Meadow Kit product (3 product bundle), create 6-7 individual social media graphics (square size). For the color scheme of the graphics, they should all be complementary with the Golden Meadow Kit bottle colors.

Note: each graphic should have one of the pictures of the bottles (3-product bundle) on it and/or one of the images with a person on it (several pics attached to choose from). I even included some real customer “before and afters” pictures…you can use them if you think the quality is good enough.

Target Market(s)

men and women looking for fast, healthy loss

Industry/Entity Type

health and wellness

Requirements
Must have
• the product is a picture of ALL 3 bottles; no single bottles will be selected

```html
<!DOCTYPE html>
<html lang="en">
<head>
<meta charset="utf-8">
<title>Golden Meadow Kit Social Media Graphics</title>
<link href="https://fonts.googleapis.com/css2?family=Montserrat:wght@300;400;500;600;700;800&display=swap" rel="stylesheet">
<style>
:root{
  --canvas:#6b6b6b;
  --ink:#1c1c1c;
  --plum:#6e3560;
  --berry:#7a2a4e;
  --rose:#d99bc5;
  --rose-soft:#f3dbe9;
  --orchid:#c774a8;
  --wine:#6b1f3a;
  --royal:#2a4a9a;
  --signal:#d8343f;
  --white:#ffffff;
}
*{margin:0;padding:0;box-sizing:border-box}
html,body{width:1200px;height:5333px;overflow:hidden;background:var(--canvas)}
body{position:relative;font-family:"Montserrat",sans-serif}
.post{position:absolute;left:120px;width:960px;height:962px;overflow:hidden;box-shadow:0 4px 10px rgba(0,0,0,.35)}
.abs{position:absolute}
.photo{position:absolute}
.bottles{background:linear-gradient(180deg,#f7f7fa 0%,#e6e8ef 60%,#c9cfe0 100%);border-radius:18px}

/* Post 1 */
.post-melt{top:103px;background:linear-gradient(135deg,#e6e1e6 0%,#f4f2f4 45%,#ffffff 100%)}
.post-melt .headline{left:62px;top:80px;font-weight:800;font-size:50px;line-height:80px;color:var(--ink);letter-spacing:1px}
.post-melt .accent{color:var(--berry)}
.post-melt .faster{letter-spacing:30px}
.post-melt .model{left:470px;top:0;width:490px;height:962px;background:linear-gradient(180deg,#b88c70 0%,#8a5f4a 45%,#3a3436 100%);clip-path:polygon(20% 0,100% 0,100% 100%,12% 100%,18% 60%,10% 40%)}

/* Post 2 */
.post-struggle{top:1144px;background:var(--white)}
.post-struggle .figure{left:0;top:0;width:960px;height:560px;background:linear-gradient(90deg,#f6e6f1 0%,#e4b9d8 50%,#f6e6f1 100%)}
.post-struggle .copy{left:0;width:960px;text-align:center;color:var(--white);font-size:48px;line-height:80px;top:665px}
.post-struggle .copy b{font-weight:700}
.post-struggle .copy .thin{font-weight:300}
.post-struggle .copy .pink{color:var(--rose);font-weight:700}

/* Post 3 */
.post-burn{top:2185px;background:var(--royal)}
.post-burn .grid{left:62px;top:70px;width:836px;height:508px;background:var(--white);padding:10px;display:grid;grid-template-columns:repeat(6,1fr);grid-template-rows:1fr 1fr;gap:6px}
.post-burn .grid div{background:linear-gradient(180deg,#7c7468,#3d3833)}
.post-burn .copy{left:0;width:960px;text-align:center;color:var(--white);font-size:62px;line-height:89px;top:655px;letter-spacing:1px}
.post-burn .copy b{font-weight:800}
.post-burn .copy .thin{font-weight:400}

/* Post 4 */
.post-natural{top:3225px;background:linear-gradient(90deg,#f5dcea 0%,#ffffff 40%,#fbeef5 100%)}
.post-natural .copy{left:56px;top:197px;font-size:46px;line-height:98px;font-weight:800;color:var(--ink)}
.post-natural .copy .soft{color:var(--orchid);font-weight:400}
.post-natural .arch{left:455px;top:45px;width:462px;height:860px;border-radius:231px 231px 200px 200px;background:linear-gradient(180deg,#6b4a3c 0%,#c4a898 45%,#efe9ec 80%,#e3dadd 100%)}
.plus{color:var(--orchid);font-size:54px;font-weight:300;position:absolute;line-height:1}

/* Post 5 */
.post-ditch{top:4266px;background:var(--wine)}
.post-ditch .copy{left:56px;top:128px;color:var(--white);font-size:36px;line-height:67px;font-weight:600}
.post-ditch .copy .thin{font-weight:400}
.post-ditch .benefits{left:56px;top:340px;list-style:none;color:var(--white);font-size:21px;font-weight:500}
.post-ditch .benefits li{display:flex;align-items:center;height:39.5px;gap:18px}
.post-ditch .portrait{left:570px;top:-40px;width:440px;height:440px;border-radius:50%;background:linear-gradient(135deg,#f6d7e4 0%,#e39ab7 55%,#f3dbe6 100%);border:8px solid var(--white)}
</style>
</head>
<body>

<section class="post post-melt">
  <svg class="abs" width="960" height="962" viewBox="0 0 960 962">
    <circle cx="940" cy="330" r="70" fill="#f4cfdf"/>
    <path d="M940 95 l20 10 -18 20z" fill="none" stroke="#b57a98" stroke-width="3"/>
    <path d="M880 760 l0 50 -45 -12z" fill="none" stroke="#b57a98" stroke-width="3"/>
    <path d="M880 850 v110 M880 890 h80" stroke="var(--berry)" stroke-width="4"/>
  </svg>
  <div class="photo model" role="img" aria-label="Smiling athletic woman holding a bathroom scale"></div>
  <div class="photo bottles" style="left:35px;top:680px;width:400px;height:250px" role="img" aria-label="Three supplement bottles of the Golden Meadow Kit"></div>
  <h1 class="abs headline">MELT AWAY<br>BELLY FAT<br><span class="accent faster">FASTER</span><br>WITH THIS<br><span class="accent">POWERFUL</span><br>TRIO!</h1>
</section>

<section class="post post-struggle">
  <div class="photo figure" role="img" aria-label="Woman measuring her waist with a tape measure, pink tint"></div>
  <svg class="abs" width="960" height="962" viewBox="0 0 960 962">
    <circle cx="855" cy="180" r="72" fill="#f1edef"/>
    <path d="M68 380 l42 8 -26 34z" fill="none" stroke="var(--plum)" stroke-width="3"/>
    <rect x="0" y="545" width="960" height="417" fill="var(--plum)"/>
    <path d="M38 630 V962 M922 600 V962 M30 640 H930" stroke="var(--rose)" stroke-width="2" fill="none"/>
    <path d="M440 962 a40 40 0 0 1 80 0" fill="#8b4f7c"/>
  </svg>
  <p class="abs copy"><b>STRUGGLING TO</b> <span class="thin">LOSE WEIGHT?</span><br><b>DISCOVER OUR ULTIMATE</b><br><span class="pink">SOLUTION!</span></p>
</section>

<section class="post post-burn">
  <svg class="abs" width="960" height="962" viewBox="0 0 960 962">
    <rect x="920" y="120" width="40" height="160" fill="var(--signal)"/>
    <path d="M582 613 h24 l-12 18z" fill="none" stroke="#ffffff" stroke-width="3"/>
    <path d="M860 632 H960 M860 642 H960" stroke="var(--signal)" stroke-width="3"/>
    <circle cx="1000" cy="912" r="60" fill="#ffffff"/>
    <path d="M0 880 a80 80 0 0 1 40 82 H0z" fill="#ffffff"/>
  </svg>
  <div class="abs grid" role="img" aria-label="Customer before and after weight loss photos">
    <div></div><div></div><div></div><div></div><div></div><div></div>
    <div></div><div></div><div></div><div></div><div></div><div></div>
  </div>
  <p class="abs copy"><b>BURN BELLY FAT FAST</b><br><span class="thin">THE 3-PART</span> <b>SOLUTION</b><br><b>YOU</b> <span class="thin">NEED NOW!</span></p>
</section>

<section class="post post-natural">
  <svg class="abs" width="960" height="962" viewBox="0 0 960 962">
    <circle cx="60" cy="130" r="260" fill="#f7e3ee"/>
  </svg>
  <div class="photo arch" role="img" aria-label="Smiling woman in a white crop top presenting three supplement bottles in a kitchen"></div>
  <h2 class="abs copy"><span class="soft">LOSE WEIGHT</span><br>NATURALLY<br>DITCH THE<br><span class="soft">PRESCRIPTION</span><br>PILLS AND<br>NEEDLES!</h2>
  <span class="plus" style="left:70px;top:830px">+</span>
  <span class="plus" style="left:6px;top:905px">+</span>
  <span class="plus" style="left:70px;top:905px">+</span>
</section>

<section class="post post-ditch">
  <svg class="abs" width="960" height="962" viewBox="0 0 960 962">
    <circle cx="-20" cy="500" r="110" fill="#7d2a4a"/>
    <path d="M0 962 V760 C260 660 420 600 620 560 C760 530 880 520 960 480 V962z" fill="#ffffff"/>
    <path d="M240 962 C360 800 560 770 960 760 V962z" fill="var(--royal)"/>
    <path d="M940 360 a22 22 0 0 0 0 44" fill="none" stroke="var(--royal)" stroke-width="4"/>
    <g stroke="#b0506f" stroke-width="3"><path d="M28 60 h24 M40 48 v24 M72 60 h24 M84 48 v24 M120 20 h24 M132 8 v24 M530 402 h24 M542 390 v24 M600 385 h24 M612 373 v24"/></g>
    <g stroke="#ffffff" stroke-width="3"><path d="M640 350 h24 M652 338 v24"/></g>
  </svg>
  <div class="photo portrait" role="img" aria-label="Close-up of a waist in pink athletic wear"></div>
  <h2 class="abs copy">Lose Weight Naturally<br>Ditch The <span class="thin">Prescription</span><br>Pills &amp; Needles!</h2>
  <ul class="abs benefits">
    <li><svg width="22" height="22" viewBox="0 0 22 22"><circle cx="11" cy="11" r="9" fill="none" stroke="#fff" stroke-width="2"/><path d="M6 11 l4 4 7 -8" fill="none" stroke="#fff" stroke-width="2.2"/></svg>Melt Stubborn Belly Fat</li>
    <li><svg width="22" height="22" viewBox="0 0 22 22"><circle cx="11" cy="11" r="9" fill="none" stroke="#fff" stroke-width="2"/><path d="M6 11 l4 4 7 -8" fill="none" stroke="#fff" stroke-width="2.2"/></svg>Reduce Bloating And Inflammation</li>
    <li><svg width="22" height="22" viewBox="0 0 22 22"><circle cx="11" cy="11" r="9" fill="none" stroke="#fff" stroke-width="2"/><path d="M6 11 l4 4 7 -8" fill="none" stroke="#fff" stroke-width="2.2"/></svg>Get That Waistline Snatched</li>
    <li><svg width="22" height="22" viewBox="0 0 22 22"><circle cx="11" cy="11" r="9" fill="none" stroke="#fff" stroke-width="2"/><path d="M6 11 l4 4 7 -8" fill="none" stroke="#fff" stroke-width="2.2"/></svg>Boost Energy And Confidence</li>
  </ul>
  <div class="photo bottles" style="left:335px;top:555px;width:590px;height:372px" role="img" aria-label="Three supplement bottles of the Golden Meadow Kit"></div>
</section>

</body>
</html>
```